hi all

Im after a new age looking business card with my company logo on it

must include these details, I would like the PH and Email to be symbols

If the colours used for card could be kept within the colours used in logo that I have supplied that would be great, if another colour is to be used dark grey would be ok. no light bulbs etc thanks

Details below to be incorporated on card

Damian Holloway

Lic E871302

PH 0219647381

E info@brightvaleelectrical.example.nz

Domestic Commercial Industrial Electricians

```html
<!DOCTYPE html>
<html lang="en">
<head>
<meta charset="utf-8">
<title>Brightvale Electrical – Business Card</title>
<link href="https://fonts.googleapis.com/css2?family=Open+Sans:ital,wght@0,400;0,600;0,700;1,400&display=swap" rel="stylesheet">
<style>
  :root {
    --brand-blue: #0e75be;
    --ink-dark: #2b2b2b;
    --ink-grey: #555555;
    --card-white: #ffffff;
    --backdrop: #3a3634;
  }
  * { box-sizing: border-box; margin: 0; padding: 0; }
  html, body { width: 1200px; height: 716px; overflow: hidden; }
  body {
    background: var(--backdrop);
    font-family: "Open Sans", Arial, sans-serif;
    display: flex;
    align-items: center;
    justify-content: center;
    gap: 40px;
  }
  .card {
    position: relative;
    width: 540px;
    height: 309px;
    overflow: hidden;
    box-shadow: 0 10px 30px rgba(0,0,0,0.45);
  }

  /* Front */
  .card-front { background: var(--brand-blue); color: var(--card-white); }
  .front-wordmark {
    position: absolute;
    left: 0; right: 0; top: 92px;
    display: flex;
    align-items: center;
    justify-content: center;
    gap: 14px;
  }
  .front-wordmark .mark-dot {
    width: 46px; height: 46px;
    border: 4px solid var(--card-white);
    border-radius: 50%;
  }
  .front-wordmark .company-name {
    font-weight: 700;
    font-size: 30px;
    line-height: 1.05;
    letter-spacing: 2px;
    text-transform: uppercase;
  }
  .tagline-row {
    position: absolute;
    left: 22px; right: 22px; bottom: 58px;
    display: flex;
    align-items: center;
    gap: 14px;
  }
  .tagline-row .rule { flex: 1; height: 1px; background: rgba(255,255,255,0.85); }
  .tagline-row .tagline { font-size: 12px; font-style: italic; white-space: nowrap; }

  /* Back */
  .card-back { background: var(--card-white); }
  .back-wordmark {
    position: absolute;
    left: 34px; top: 40px;
    display: flex;
    align-items: center;
    gap: 10px;
  }
  .back-wordmark .mark-dot {
    width: 30px; height: 30px;
    border: 3px solid var(--ink-dark);
    border-radius: 50%;
  }
  .back-wordmark .company-name {
    font-weight: 700;
    font-size: 19px;
    line-height: 1.05;
    letter-spacing: 1.5px;
    text-transform: uppercase;
    color: var(--brand-blue);
  }
  .person { position: absolute; left: 34px; top: 128px; }
  .person .name {
    font-weight: 700;
    font-size: 19px;
    color: var(--brand-blue);
    text-transform: uppercase;
    letter-spacing: 0.5px;
  }
  .person .role { font-size: 12px; color: var(--ink-grey); margin-top: 2px; }

  .contact {
    position: absolute;
    left: 286px; top: 186px;
    list-style: none;
    font-size: 13px;
    color: var(--ink-dark);
  }
  .contact li { display: flex; align-items: center; gap: 7px; line-height: 22px; }
  .contact .licence { color: var(--brand-blue); padding-left: 18px; }
  .contact svg { width: 11px; height: 11px; fill: var(--brand-blue); flex: none; }

  .bottom-band { position: absolute; left: 0; bottom: 0; width: 540px; height: 60px; }
  .bottom-band path { fill: var(--brand-blue); }
</style>
</head>
<body>
  <section class="card card-front">
    <div class="front-wordmark">
      <span class="mark-dot"></span>
      <span class="company-name">Brightvale<br>Electrical</span>
    </div>
    <div class="tagline-row">
      <span class="rule"></span>
      <span class="tagline">Domestic Commercial Industrial Electricians</span>
      <span class="rule"></span>
    </div>
  </section>

  <section class="card card-back">
    <div class="back-wordmark">
      <span class="mark-dot"></span>
      <span class="company-name">Brightvale<br>Electrical</span>
    </div>
    <div class="person">
      <p class="name">Damian Holloway</p>
      <p class="role">Manager</p>
    </div>
    <ul class="contact">
      <li class="licence">Lic E871302</li>
      <li>
        <svg viewBox="0 0 24 24" aria-hidden="true"><path d="M6.6 10.8a15.1 15.1 0 0 0 6.6 6.6l2.2-2.2c.3-.3.7-.4 1-.2 1.1.4 2.3.6 3.6.6.6 0 1 .4 1 1V20c0 .6-.4 1-1 1A17 17 0 0 1 3 4c0-.6.4-1 1-1h3.5c.6 0 1 .4 1 1 0 1.3.2 2.5.6 3.6.1.3 0 .7-.2 1z"/></svg>
        <span>0219647381</span>
      </li>
      <li>
        <svg viewBox="0 0 24 24" aria-hidden="true"><path d="M2 5h20v14H2zm2 2v.4l8 5.2 8-5.2V7zm0 2.8V17h16V9.8l-8 5.2z"/></svg>
        <span>info@brightvaleelectrical.example.nz</span>
      </li>
    </ul>
    <svg class="bottom-band" viewBox="0 0 540 60" preserveAspectRatio="none" aria-hidden="true">
      <path d="M210 60 C240 20 270 18 310 22 L540 40 L540 60 Z"/>
    </svg>
  </section>
</body>
</html>
```